KV HOLDWELL GROUP LETTERHEAD

I need letterhead for "KV Holdwell group LLC" ...

logo attached to project...

Company Info:
845 North Marlow Avenue, Suite 7B
Chicago, Illinois 60611
ofc 312-555-0184
facsimile 312-555-0172
www.kvholdwellgroup.example
info@kvholdwellgroup.example

I have multiple projects listed.. see below:

Business cards for ashford lane equity llc
letterhead
envelopes

Business cards for KV Holdwell LLC
letterhead
envelopes

```html
<!DOCTYPE html>
<html lang="en">
<head>
<meta charset="utf-8">
<title>KV Holdwell Group LLC — Letterhead</title>
<link rel="stylesheet" href="https://fonts.googleapis.com/css2?family=Arimo:wght@400;700&display=swap">
<style>
  :root {
    --backdrop: #d9d9d9;
    --paper: #ffffff;
    --navy: #1f3a7a;
    --ink: #7a7a7a;
    --ink-soft: #9a9a9a;
  }
  * { box-sizing: border-box; margin: 0; padding: 0; }
  html, body {
    width: 1200px; height: 1078px; overflow: hidden;
    background: var(--backdrop);
    font-family: "Arimo", Arial, sans-serif;
  }
  .letterhead {
    position: absolute; left: 198px; top: 19px;
    width: 804px; height: 1040px;
    background: var(--paper);
    box-shadow: 0 4px 14px rgba(0,0,0,.12);
  }
  .contact {
    position: absolute; left: 520px; top: 70px;
    font-size: 8px; line-height: 12px; color: var(--ink-soft);
    font-style: normal;
  }
  .contact-label { color: var(--navy); font-weight: 700; margin-right: 4px; }
  .brand {
    position: absolute; left: 78px; top: 200px;
    display: flex; align-items: center; gap: 10px;
  }
  .brand-dot {
    flex: none;
    width: 14px; height: 14px; border-radius: 50%;
    background: var(--navy);
  }
  .brand-name {
    font-size: 20px; font-weight: 400; letter-spacing: .04em;
    color: var(--navy); text-transform: uppercase; white-space: nowrap;
  }
  .letter-body {
    position: absolute; left: 96px; top: 310px; width: 600px;
    font-size: 10.5px; line-height: 14px; color: var(--ink);
  }
  .salutation { margin-bottom: 22px; }
  .letter-body p + p { margin-top: 22px; }
  .footer-brand {
    position: absolute; right: 70px; bottom: 72px;
    display: flex; align-items: center; gap: 6px;
  }
  .footer-brand .brand-dot { width: 7px; height: 7px; }
  .footer-brand .brand-name { font-size: 9px; }
  .footer-rule {
    position: absolute; left: 0; bottom: 44px; width: 804px; height: 22px;
  }
</style>
</head>
<body>
  <main class="letterhead">
    <address class="contact">
      845 North Marlow Avenue, Suite 7B<br>
      Chicago, Illinois 60611<br>
      <span class="contact-label">ofc</span>312-555-0184<br>
      <span class="contact-label">facsimile</span>312-555-0172<br>
      <span class="contact-label">WEB</span>www.kvholdwellgroup.example<br>
      <span class="contact-label">Email</span>info@kvholdwellgroup.example
    </address>

    <div class="brand">
      <span class="brand-dot"></span>
      <span class="brand-name">KV Holdwell Group LLC</span>
    </div>

    <section class="letter-body">
      <div class="salutation">The standard chunk of<br>The standard chunk of</div>
      <p>We are pleased to share an update on our firm and the work ahead for the coming year. Our team continues to focus on long term value, careful research and clear communication with every partner we serve. This letter outlines the steps we have taken, the results we have seen so far and the priorities that will guide our decisions in the months to come. We welcome your questions at any time.</p>
      <p>Over the past quarter we completed two new investments and expanded our office to support a growing group of clients. Each decision followed the same disciplined review process described in our annual report and partner guide.</p>
      <p>Looking forward, we will keep our approach simple and patient. We plan to strengthen relationships with local operators, review each holding on a regular schedule and report our progress openly. Thank you for the trust you place in our team. We look forward to speaking with you soon and to building on the strong foundation we share together in the year ahead.</p>
    </section>

    <div class="footer-brand">
      <span class="brand-dot"></span>
      <span class="brand-name">KV Holdwell Group LLC</span>
    </div>
    <svg class="footer-rule" viewBox="0 0 804 22" preserveAspectRatio="none" aria-hidden="true">
      <rect x="0" y="2" width="804" height="4" fill="#1f3a7a"/>
      <rect x="0" y="10" width="804" height="1.5" fill="#1f3a7a"/>
      <rect x="0" y="15" width="804" height="4" fill="#1f3a7a"/>
    </svg>
  </main>
</body>
</html>
```